Greek Souvlaki Restaurant Menu Design

We would like to redesign our menu (at the moment just a price-list without any graphics) and create something more fun.

You can find all the items we are offering at the following link / our e-shop:
https://olivebranchkitchen.example/orders/en/order/
I have also attached a printout of the above with hand written notes on the sections and items that will be included.

Our menu is divided to a couple of parts:
- Souvlaki Bar and Grill
- Authentic Greek Cuisine
- Wine List
- Desserts
- Bakaliko

This project will take on the first part of our menu, which is the Souvlaki Bar and Grill. If we are happy with your design, we will then develop the rest of our menu.

Souvlaki Bar and Grill
---------------------------

Our souvlaki can be customised to the customer requirements. The following links have similar set ups:

WOW!Patty
https://gr.pinboardly.example/pin/100000000000000001/
I like the way they have set it up, but the graphics and colours used are not my thing. I also like they way they have split up the steps, choose, top it of, etc.

The Krokk
https://gr.pinboardly.example/pin/100000000000000002/
I hate the step 1,2,3 on the left side. It does not make it playful. Like the fact that they have used pictures of the ingredients.

https://gr.pinboardly.example/pin/100000000000000003/
Hate the graphics, like the concept.

-------------

First Sections: Our Souvliaki Pita Wrap

The steps to customise a souvlaki can be found on the following link:
https://olivebranchkitchen.example/orders/en/order/ and choose pita wrap.

Most of the one side of our Souvliaki/Grill menu should be dedicated to our Pita Wraps.

It should have a small description of the Greek Souvlaki Pita Wrap. Something along the lines of "Get a whole meal all wrapped up with our delicious Greek Pita Wraps. Containing protein, sauce and salad". Improvements of this line are welcome.

It should then have the steps to customise it.

Step One.
Choose Base:
1. Chicken Skewer
2. Pork Skewer
3. etc
Price and options can be found on the above link on our website

Step Two.
Add one of our delicious home made sauces.
Options can be found on our website.

Step Three
Finalise it with the ingredients of your choice.
The customer can select multiple incredients

Step Four.
Feeling Hungry? Add extras:
Extras and Prices can be found on the link provided.

Buy two wraps and save. Takeaway only!
You will find this option as "Double Souvlaki Pita Wrap Offer."
Instead of 2x5.5 = £11 pay £10.5. This offer should also be mentioned somewhere on this section.

-----

Second Section - Our Platters

Skewers Platter and Gyros Platter

Options can be found by clicking on the items on the link provided.

Extras and Pita Bread option are common. Meat options are different and skewers have a choice of side. Meat options have 2/3 skewers and 200/300 grams of gyros, so they can probably be combined somehow.

These section can also be called Naked / Open Souvlaki Platters

Third Section
From Our Grill

All options from this section together with modifiers (can be see if you click on each item). I would like pictures from each item.

Forth Section
Meal Deals, starter combo and Set Menu.

Meal Deal for 1/2 and 4 are wraps with extras. The for 4 is not on the pdf and will be up on our website soon, so please check. I think those are easy to e incorporated next to the pita wrap section as upgrades to save.

Set menus are various items.

If they can fit on this page somehow we incorporate them, if not we can make a separate page with the offers / meals deals. If a separate page is created them the meal deal from our kitchen and vegetarean set menu should also be included.

Fifth Section
Salads and Starter

I would like all options from Hot and Cold starter and our salad. I would like pictures next to all options, if possible.

-----

Final notes/ideas.

Wraps, platters and grill could be one page front and back. Salads and starters could be a different page(s) or sections.

The menu should be easily updated and we would like a format where we can update prices and descriptions.

Prices and descriptions can be found on the link provided.

Feel free to improve our descriptions and titles. Please do mention where you made improvements, so we can approve them.

Our kitchen, dessert and wine menu will be given as a separate project and priority will be given to the person that won this competition.

If you need better quality pictures please let us know, most of the pictures we do have them in raw format too.

------

Some designs that I like. To give you an idea of the design I would like to see:

https://www.craftmarketly.example/listing/100000001/american-menu-restaurant-cafe-menus
I would love to see something like that for the grill/salad/starter side of our menu, since it has space for pictures.

https://gr.pinboardly.example/pin/100000000000000004/
I would love to see something like that, where the incredients of a souvlaki come together. This is optional and does not have to be there.

https://gr.pinboardly.example/pin/100000000000000005/

https://gr.pinboardly.example/pin/100000000000000006/

https://gr.pinboardly.example/pin/100000000000000007/

https://gr.pinboardly.example/pin/100000000000000008/

Target Market(s)

London

Font styles to use
Serif
Sans Serif

Colors
abd037
3277b5
33a6d7

Requirements
Must have
• Build your own souvlaki section. See description for examples.

Pictures for starters and salads.

Should be elegant
Nice to have
• Incorporate our relevant meal deals on the souvlaki pita section

```html
<!DOCTYPE html>
<html lang="en">
<head>
<meta charset="utf-8">
<title>Souvlaki Pita Wrap Menu – Harbour Lane Kitchen</title>
<link rel="stylesheet" href="https://fonts.googleapis.com/css2?family=Catamaran:wght@400;500;700;800;900&family=Open+Sans:ital,wght@1,700&family=Kaushan+Script&family=Raleway:wght@400&display=swap">
<style>
  :root {
    --bg-top: #5a86c2;
    --bg-mid: #6690c9;
    --bg-bottom: #5b86c0;
    --panel: #3153a8;
    --band: #2e4fa2;
    --gold: #8a7a1e;
    --white: #ffffff;
    --ink-blue: #2b4a9c;
    --line: rgba(255,255,255,0.92);
    --photo-a: #c89a62;
    --photo-b: #8d6a3e;
    --plate: #eef0f2;
  }
  * { box-sizing: border-box; margin: 0; padding: 0; }
  html, body { width: 1200px; height: 1200px; overflow: hidden; }
  body {
    position: relative;
    background: linear-gradient(180deg, var(--bg-top) 0%, var(--bg-mid) 50%, var(--bg-bottom) 100%);
    font-family: "Catamaran", sans-serif;
    color: var(--white);
  }
  .abs { position: absolute; }

  .page-title {
    left: 63px; top: 50px;
    font-family: "Raleway", sans-serif;
    font-size: 33px; letter-spacing: 6px; font-weight: 400;
  }
  .brand {
    right: 40px; top: 44px;
    font-size: 20px; font-weight: 700; line-height: 24px;
  }

  .hero-photo {
    left: 60px; top: 140px; width: 465px; height: 335px;
    border-radius: 30px 60px 40px 40px;
    background: radial-gradient(ellipse at 45% 50%, var(--photo-a) 0%, var(--photo-b) 55%, var(--plate) 80%, rgba(238,240,242,0) 100%);
  }

  .title-band {
    left: 500px; top: 266px; width: 700px; height: 52px;
    background: var(--band);
  }
  .product-name {
    left: 545px; top: 268px;
    font-size: 32px; font-weight: 800; line-height: 48px;
  }
  .product-price {
    left: 972px; top: 266px;
    font-size: 39px; font-weight: 800; line-height: 52px;
  }
  .product-desc {
    left: 545px; top: 338px; width: 305px;
    font-size: 22px; line-height: 28px; font-weight: 400;
  }

  .section-rule {
    left: 138px; top: 504px; width: 922px; height: 24px;
    display: flex; align-items: center; gap: 18px;
  }
  .section-rule::before, .section-rule::after {
    content: ""; flex: 1; height: 2px; background: var(--line);
  }
  .section-rule span {
    font-weight: 800; font-size: 21px; letter-spacing: 9px;
  }

  .step {
    left: 107px; width: 985px;
    background: var(--panel);
    border-radius: 14px;
  }
  .step-label {
    position: absolute; left: 11px; top: 4px;
    font-family: "Open Sans", sans-serif; font-style: italic; font-weight: 700;
    font-size: 21px;
  }
  .step-head {
    position: absolute; left: 80px; right: 80px; top: 0; height: 26px;
    background: linear-gradient(90deg, rgba(138,122,30,0) 0%, var(--gold) 30%, var(--gold) 70%, rgba(138,122,30,0) 100%);
    text-align: center; font-weight: 800; font-size: 20px; line-height: 29px;
  }
  .step-head .hungry {
    font-family: "Kaushan Script", cursive; font-weight: 400; font-size: 18px;
    margin-right: 10px;
  }
  .options {
    position: absolute; left: 0; right: 0;
    text-align: center; font-size: 22px; line-height: 30px;
  }
  .options .opt::before { content: "•"; margin: 0 14px 0 16px; font-size: 16px; }

  .step-base { top: 533px; height: 136px; }
  .step-base .options { top: 35px; }
  .step-sauce { top: 687px; height: 81px; }
  .step-sauce .options { top: 35px; }
  .step-ingredients { top: 786px; height: 80px; }
  .step-ingredients .options { top: 35px; }
  .step-extras { top: 884px; height: 104px; }
  .step-extras .options { top: 36px; }

  .offer-lead {
    left: 267px; top: 1046px; color: var(--ink-blue);
    font-weight: 800; line-height: 1;
  }
  .offer-lead .small { display: block; font-size: 21px; }
  .offer-lead .big { display: block; font-size: 60px; font-weight: 900; margin-top: -6px; }
  .offer-photo {
    left: 466px; top: 1035px; width: 128px; height: 100px;
    border-radius: 50%;
    background: radial-gradient(ellipse at center, var(--photo-a) 0%, var(--photo-b) 50%, var(--plate) 75%);
  }
  .offer-detail { left: 605px; top: 1048px; color: var(--ink-blue); }
  .offer-detail .was { display: block; font-size: 22px; letter-spacing: 6.5px; line-height: 26px; }
  .offer-detail .now { display: block; font-size: 41px; line-height: 50px; font-weight: 500; margin-top: 4px; }
  .offer-detail .now b { font-weight: 900; }
</style>
</head>
<body>
  <h1 class="abs page-title">Our Souvliaki Pita Wrap</h1>
  <div class="abs brand">Harbour Lane Kitchen</div>

  <div class="abs hero-photo" role="img" aria-label="Photo of a Greek souvlaki pita wrap with fries, tomato and tzatziki in a paper sleeve on a plate"></div>

  <div class="abs title-band"></div>
  <h2 class="abs product-name">Greek Souvlaki Pita Wrap</h2>
  <div class="abs product-price">£ 5.50</div>
  <p class="abs product-desc">Get a whole meal all wrapped up with our delicious Greek Pita Wraps. Containing protein, sauce and salad</p>

  <div class="abs section-rule"><span>MAKE IT YOUR OWN</span></div>

  <section class="abs step step-base">
    <div class="step-label">Step 1</div>
    <div class="step-head">CHOOSE BASE</div>
    <div class="options">
      <div><span class="opt">Chicken + £ 0.50</span><span class="opt">Pork + £ 0.50</span><span class="opt">Gyros Chicken + £ 1.50</span></div>
      <div><span class="opt">Gyros Pork + £ 1.50</span><span class="opt">Mixed Gyros (Chicken &amp; Pork) + £ 2.00</span><span class="opt">Kebab (Lamb+Beef) + £ 0.50</span></div>
      <div><span class="opt">Sausage + £ 0.50</span><span class="opt">Haloumi (V) + £ 0.50</span><span class="opt">No Base (V)</span></div>
    </div>
  </section>

  <section class="abs step step-sauce">
    <div class="step-label">Step 2</div>
    <div class="step-head">ADD ONE OF OUR DELICIOUS HOME MADE SAUCES</div>
    <div class="options">
      <span class="opt">Tzatziki (V)</span><span class="opt">Tyrokafteri (V)</span><span class="opt">Burher Sauce</span><span class="opt">No Sauce</span>
    </div>
  </section>

  <section class="abs step step-ingredients">
    <div class="step-label">Step 3</div>
    <div class="step-head">FINALISE IT WITH THE INGREDIENTS OF YOUR CHOICE</div>
    <div class="options">
      <span class="opt">Fries</span><span class="opt">Tomatoes</span><span class="opt">Onions</span><span class="opt">No Ingredients</span>
    </div>
  </section>

  <section class="abs step step-extras">
    <div class="step-label">Step 4</div>
    <div class="step-head"><span class="hungry">Feeling Hungry?</span>ADD EXTRAS</div>
    <div class="options">
      <div><span class="opt">Double Pita Breed &nbsp;£ 1.00</span><span class="opt">Add Pork Skewer £ &nbsp;2.50</span><span class="opt">Add Chicken Skewer £ &nbsp;2.50</span></div>
      <div><span class="opt">Add Kebab (Lamb+Beef) £ &nbsp;2.50</span><span class="opt">Add Sausage &nbsp;£ 2.50</span><span class="opt">Add Haloumi £ 1.90</span></div>
    </div>
  </section>

  <div class="abs offer-lead"><span class="small">BUY TWO WRAPS</span><span class="big">&amp; save</span></div>
  <div class="abs offer-photo" role="img" aria-label="Photo of two souvlaki pita wraps side by side on a plate"></div>
  <div class="abs offer-detail"><span class="was">Instead of 2x5.5 = £11</span><span class="now">PAY ONLY <b>£10.50</b></span></div>
</body>
</html>
```